Harborline Motors LLC

Car Dealer Customer Service
Address: 2741 Linden Avenue, Shelbyville, TN 37162
web: www.harborlinemotorstn.net
email: harborlinemotorstn@mailbox-example.net
Phone: (931) 555-0148
Phone: (629) 555-0173

```html
<!DOCTYPE html>
<html lang="en">
<head>
<meta charset="utf-8">
<title>Harborline Motors LLC – Business Card</title>
<link rel="stylesheet" href="https://fonts.googleapis.com/css2?family=Montserrat:wght@700;800&family=Oswald:wght@600&family=Poppins:wght@400&display=swap">
<style>
  :root {
    --page: #2b2b2b;
    --blue: #1f78ad;
    --blue-deep: #176b9e;
    --gold: #e1a43a;
    --white: #ffffff;
    --paper: #f1f1f1;
    --ink: #1c1c1c;
    --band-text: #e9eef3;
  }
  * { margin: 0; padding: 0; box-sizing: border-box; }
  html, body { width: 1200px; height: 1138px; overflow: hidden; }
  body { background: var(--page); position: relative; font-family: "Poppins", sans-serif; }

  .card {
    position: absolute;
    width: 620px;
    height: 376px;
    border-radius: 16px;
    overflow: hidden;
  }

  /* Front side */
  .card--front {
    left: 274px; top: 186px;
    background: linear-gradient(135deg, var(--blue-deep), var(--blue));
  }
  .front__mark {
    position: absolute;
    left: -150px; top: 28px;
    width: 320px; height: 320px;
    border-radius: 50%;
    background: var(--white);
  }
  .front__name {
    position: absolute;
    right: 40px; top: 58px;
    font-family: "Montserrat", sans-serif;
    font-weight: 800;
    font-size: 29px;
    letter-spacing: 0.5px;
    color: var(--white);
    text-transform: uppercase;
  }
  .front__web {
    position: absolute;
    right: 42px; bottom: 34px;
    font-size: 15.5px;
    color: var(--white);
  }

  /* Back side */
  .card--back {
    left: 276px; top: 608px;
    width: 618px; height: 374px;
    background: var(--paper);
    text-align: center;
  }
  .back__mark {
    position: absolute;
    left: 259px; top: 44px;
    width: 100px; height: 100px;
    border-radius: 50%;
    background: var(--blue);
  }
  .back__name {
    position: absolute;
    left: 0; right: 0; top: 174px;
    font-family: "Montserrat", sans-serif;
    font-weight: 800;
    font-size: 30px;
    color: var(--blue);
    text-transform: uppercase;
    letter-spacing: 0.5px;
  }
  .back__tagline {
    position: absolute;
    left: 0; right: 0; top: 235px;
    font-size: 15px;
    color: var(--ink);
  }
  .back__band {
    position: absolute;
    left: 0; right: 0; top: 260px;
    height: 44px;
    background: var(--blue);
    display: flex;
    justify-content: center;
    align-items: center;
    gap: 18px;
  }
  .phone {
    display: flex;
    align-items: center;
    gap: 10px;
    font-family: "Oswald", sans-serif;
    font-weight: 600;
    font-size: 31px;
    color: var(--band-text);
  }
  .phone__icon { width: 30px; height: 30px; }
  .back__address, .back__links {
    position: absolute;
    left: 0; right: 0;
    font-size: 15px;
    color: var(--ink);
  }
  .back__address { top: 312px; }
  .back__links { top: 333px; }
</style>
</head>
<body>

<section class="card card--front" aria-label="Card front">
  <div class="front__mark"></div>
  <h1 class="front__name">Harborline Motors</h1>
  <p class="front__web">www.harborlinemotorstn.net</p>
</section>

<section class="card card--back" aria-label="Card back">
  <div class="back__mark"></div>
  <h2 class="back__name">Harborline Motors</h2>
  <p class="back__tagline">Car Dealer Customer Service</p>
  <div class="back__band">
    <span class="phone">
      <svg class="phone__icon" viewBox="0 0 30 30" aria-hidden="true">
        <circle cx="15" cy="15" r="13" fill="none" stroke="#e1a43a" stroke-width="2.4"/>
        <path d="M10.5 8.5l2.6-.4 1.4 3.4-1.6 1.3c.8 1.8 2.2 3.2 4 4l1.3-1.6 3.4 1.4-.4 2.6c-.2.7-.9 1.2-1.7 1.1-5.3-.6-9.5-4.8-10.1-10.1-.1-.8.4-1.5 1.1-1.7z" fill="#e1a43a"/>
      </svg>
      931-555-0148
    </span>
    <span class="phone">
      <svg class="phone__icon" viewBox="0 0 30 30" aria-hidden="true">
        <circle cx="15" cy="15" r="13" fill="none" stroke="#e1a43a" stroke-width="2.4"/>
        <path d="M10.5 8.5l2.6-.4 1.4 3.4-1.6 1.3c.8 1.8 2.2 3.2 4 4l1.3-1.6 3.4 1.4-.4 2.6c-.2.7-.9 1.2-1.7 1.1-5.3-.6-9.5-4.8-10.1-10.1-.1-.8.4-1.5 1.1-1.7z" fill="#e1a43a"/>
      </svg>
      629-555-0173
    </span>
  </div>
  <p class="back__address">2741 Linden Avenue, Shelbyville, TN 37162</p>
  <p class="back__links">www.harborlinemotorstn.net &nbsp;|&nbsp; harborlinemotorstn@mailbox-example.net</p>
</section>

</body>
</html>
```